Business Card Design - Local Discount Club

Looking for a fun business card for a local discount club. One side should be the logo only and the other should be have :

Name
Title
Phone, Email
Website

```html
<!DOCTYPE html>
<html lang="en">
<head>
<meta charset="utf-8">
<title>The Bayside Club Card – Business Card</title>
<link rel="stylesheet" href="https://fonts.googleapis.com/css2?family=Poppins:wght@400;500;700&display=swap">
<style>
  :root {
    --bg: #c9c9c9;
    --card: #fbfbfb;
    --navy: #3350b8;
    --blue-text: #3a56c0;
    --cyan: #4fd3ef;
    --green: #8ff07f;
    --ink: #2b3f8f;
  }
  * { margin: 0; padding: 0; box-sizing: border-box; }
  html, body { width: 1200px; height: 675px; overflow: hidden; }
  body {
    background: var(--bg);
    font-family: "Poppins", sans-serif;
    position: relative;
  }
  .card {
    position: absolute;
    top: 189px;
    width: 520px;
    height: 297px;
    background: var(--card);
    border-radius: 14px;
    overflow: hidden;
    box-shadow: 0 10px 24px rgba(0,0,0,0.18);
  }
  .card--front { left: 50px; }
  .card--back { left: 630px; }
  .card__bands { position: absolute; inset: 0; width: 100%; height: 100%; }
  .dot { position: absolute; border-radius: 50%; }
  .dot--green { background: var(--green); }
  .dot--cyan { background: var(--cyan); }
  .dot--navy { background: var(--navy); }

  .brand {
    position: absolute;
    display: flex;
    align-items: center;
    gap: 10px;
    color: var(--navy);
    font-weight: 700;
    line-height: 1.05;
    text-transform: uppercase;
  }
  .brand__mark { width: 14px; height: 14px; border-radius: 50%; background: var(--navy); flex: none; }
  .card--front .brand { left: 175px; top: 120px; font-size: 30px; }
  .card--back .brand { right: 34px; top: 118px; font-size: 22px; }

  .contact {
    position: absolute;
    left: 30px; top: 58px;
    list-style: none;
    padding-left: 14px;
    border-left: 1.5px solid var(--navy);
    font-size: 12px;
    color: var(--ink);
  }
  .contact li { display: flex; align-items: center; gap: 8px; margin: 4px 0; }
  .contact svg { width: 12px; height: 12px; fill: var(--navy); flex: none; }
  .address {
    position: absolute;
    left: 44px; bottom: 52px;
    display: flex; gap: 8px; align-items: center;
    font-size: 12px; color: var(--ink); line-height: 1.35;
  }
  .address svg { width: 14px; height: 18px; fill: var(--navy); }
  .person {
    position: absolute;
    right: 60px; bottom: 50px;
    text-align: right;
    color: var(--navy);
  }
  .person__name { font-weight: 700; font-size: 20px; letter-spacing: 0.5px; }
  .person__title { font-size: 9px; letter-spacing: 1px; text-transform: uppercase; }
</style>
</head>
<body>

<section class="card card--front" aria-label="Card front">
  <svg class="card__bands" viewBox="0 0 520 297" preserveAspectRatio="none" aria-hidden="true">
    <path d="M0,0 H520 V14 C420,14 140,12 60,22 C20,28 6,60 0,170 Z" fill="var(--navy)"/>
    <path d="M0,180 C6,70 20,36 62,30 C150,18 360,22 520,110" fill="none" stroke="var(--green)" stroke-width="3"/>
    <path d="M0,248 C150,254 350,260 520,262 V297 H0 Z" fill="var(--navy)"/>
    <path d="M0,260 C150,266 350,272 520,274" fill="none" stroke="var(--cyan)" stroke-width="4"/>
  </svg>
  <span class="dot dot--green" style="left:142px;top:44px;width:22px;height:22px"></span>
  <span class="dot dot--cyan" style="left:196px;top:46px;width:24px;height:24px"></span>
  <span class="dot dot--navy" style="left:148px;top:86px;width:38px;height:38px"></span>
  <div class="brand">
    <span class="brand__name">The Bayside<br>Club Card</span>
    <span class="brand__mark"></span>
  </div>
</section>

<section class="card card--back" aria-label="Card back">
  <svg class="card__bands" viewBox="0 0 520 297" preserveAspectRatio="none" aria-hidden="true">
    <path d="M0,0 H520 V130 C512,40 490,22 440,20 C320,16 120,16 0,22 Z" fill="var(--navy)"/>
    <path d="M0,32 C140,26 330,26 436,30 C486,32 504,52 510,140" fill="none" stroke="var(--green)" stroke-width="3"/>
    <path d="M0,258 C160,262 360,266 520,262 V297 H0 Z" fill="var(--navy)"/>
    <path d="M0,270 C160,274 360,278 520,274" fill="none" stroke="var(--cyan)" stroke-width="4"/>
  </svg>
  <span class="dot dot--green" style="left:250px;top:46px;width:18px;height:18px"></span>
  <span class="dot dot--cyan" style="left:292px;top:54px;width:22px;height:22px"></span>
  <span class="dot dot--navy" style="left:246px;top:86px;width:36px;height:36px"></span>

  <ul class="contact">
    <li><svg viewBox="0 0 24 24"><path d="M6.6 10.8a15 15 0 0 0 6.6 6.6l2.2-2.2a1 1 0 0 1 1-.25 11 11 0 0 0 3.6.6 1 1 0 0 1 1 1V20a1 1 0 0 1-1 1A17 17 0 0 1 3 4a1 1 0 0 1 1-1h3.5a1 1 0 0 1 1 1c0 1.25.2 2.45.6 3.6a1 1 0 0 1-.25 1z"/></svg>000-000-0000</li>
    <li><svg viewBox="0 0 24 24"><path d="M2 5h20v14H2z M4 7v.5l8 5 8-5V7z" fill-rule="evenodd"/></svg>info@mail.com</li>
    <li><svg viewBox="0 0 24 24"><path d="M12 2a10 10 0 1 0 0 20 10 10 0 0 0 0-20zm0 2c.9 0 2.2 2 2.7 5H9.3C9.8 6 11.1 4 12 4zM4.3 11h4.8a17 17 0 0 0 0 2H4.3a8 8 0 0 1 0-2zm10.6 0h4.8a8 8 0 0 1 0 2h-4.8a17 17 0 0 0 0-2zM9.3 15h5.4c-.5 3-1.8 5-2.7 5s-2.2-2-2.7-5z"/></svg>www.example.com</li>
  </ul>

  <div class="brand">
    <span class="brand__name">The Bayside<br>Club Card</span>
    <span class="brand__mark"></span>
  </div>

  <div class="address">
    <svg viewBox="0 0 14 18"><path d="M7 0a7 7 0 0 0-7 7c0 5 7 11 7 11s7-6 7-11a7 7 0 0 0-7-7zm0 10a3 3 0 1 1 0-6 3 3 0 0 1 0 6z"/></svg>
    <div>Address Line 1<br>Address Line 2</div>
  </div>

  <div class="person">
    <div class="person__name">NAME</div>
    <div class="person__title">Owner</div>
  </div>
</section>

</body>
</html>
```